Rick Dalberson Postcard

We are having a show of this painters original artwork at our gallery next month and he is also doing a painting demonstration and we would like a postcard to send out to his collectors before the show. Info for postcard shown below

1) A show of new and original artwork by painter Rick Dalberson will be featured artist in our Lantern Gallery from August 22- September 18

2) A reception at Pinecrest Harbor Galleries to meet the artist will be held from 4-7 pm on Saturday, September 1 with an artist introduction and brief talk about his show at 5 pm.

3) A Rick Dalberson oil painting demonstration will take place on Sunday, September 2 from 1-3 pm in the gallery courtyard. Refreshments will be served and all are welcome.

Target Market(s)

Our customers who have purchased his work before, visitors to our gallery

Industry/Entity Type

Art Gallery

Requirements
Must have
• 1) A show of new and original artwork by painter Rick Dalberson will be featured artist in our Lantern Gallery from August 22- September 18
• 2) A reception at Pinecrest Harbor Galleries to meet the artist will be held from 4-7 pm on Saturday, September 1 with an artist introduction and brief talk about his show at 5 pm.
• 3) A Rick Dalberson oil painting demonstration will take place on Sunday, September 2 from 1-3 pm in the gallery courtyard. Refreshments will be served and all are welcome.

```html
<!DOCTYPE html>
<html lang="en">
<head>
<meta charset="utf-8">
<title>Rick Dalberson Postcard</title>
<link rel="stylesheet" href="https://fonts.googleapis.com/css2?family=EB+Garamond:ital,wght@0,400;0,500;1,400&family=Source+Sans+3:wght@400;600&display=swap">
<style>
  :root {
    --page: #dad8d3;
    --card: #eeece6;
    --band: #76695a;
    --band-text: #ffffff;
    --ink: #5e5347;
    --quote: #6e6862;
    --rule: #8a7f73;
    --line: #9c958d;
    --shadow: rgba(40, 30, 20, 0.28);
    --serif: "EB Garamond", Georgia, serif;
    --sans: "Source Sans 3", Arial, sans-serif;
  }
  * { box-sizing: border-box; margin: 0; padding: 0; }
  html, body { width: 948px; height: 1200px; overflow: hidden; }
  body { background: var(--page); font-family: var(--sans); color: var(--ink); position: relative; }

  .postcard {
    position: absolute; left: 94px; width: 760px; height: 493px;
    background: var(--card); box-shadow: 0 3px 10px var(--shadow); overflow: hidden;
  }
  .postcard--front { top: 80px; }
  .postcard--back { top: 621px; }

  .gallery-name {
    position: absolute; text-align: center; font-family: var(--serif);
    font-weight: 500; color: var(--band); letter-spacing: 2px; text-transform: uppercase; line-height: 1.15;
  }

  /* Front */
  .feature-painting {
    position: absolute; left: 10px; top: 16px; width: 336px; height: 456px;
    border: 6px solid #fff; transform: rotate(-4deg);
    box-shadow: 0 2px 8px var(--shadow);
    background: linear-gradient(160deg, #7d7a4c 0%, #c9c6a2 30%, #6b3e2c 50%, #8f9a3f 72%, #c8c98a 100%);
  }
  .postcard--front .gallery-name { left: 380px; width: 340px; top: 52px; font-size: 24px; }
  .title-band {
    position: absolute; background: var(--band); color: var(--band-text); text-align: center;
    border-top: 2px solid #fff; border-bottom: 2px solid #fff;
    display: flex; flex-direction: column; justify-content: center; align-items: center;
  }
  .postcard--front .title-band { left: 319px; right: 0; top: 134px; height: 106px; }
  .artist-name { font-family: var(--serif); font-weight: 400; line-height: 1; }
  .postcard--front .artist-name { font-size: 42px; }
  .artist-role { font-size: 13px; margin-top: 6px; line-height: 1.1; }
  .event-type { font-family: var(--serif); font-size: 14px; margin-top: 8px; letter-spacing: 0.2px; line-height: 1.1; }

  .event-details { position: absolute; text-align: center; font-size: 14px; line-height: 1.3; }
  .postcard--front .event-details { left: 330px; width: 420px; top: 255px; }
  .artist-quote {
    position: absolute; left: 363px; width: 385px; top: 320px;
    font-family: var(--serif); font-style: italic; font-size: 11.6px; line-height: 1.38;
    color: var(--quote); text-align: justify;
  }
  .artist-quote .mark { font-style: normal; font-size: 20px; line-height: 0; color: #a8a29b; vertical-align: -6px; margin-right: 3px; }
  .web-ribbon {
    position: absolute; left: 430px; top: 422px; width: 240px; height: 26px;
    background: var(--band); color: #fff; font-size: 13.5px; text-align: center; line-height: 26px;
    clip-path: polygon(0 0, 100% 0, 96% 50%, 100% 100%, 0 100%, 4% 50%);
  }
  .web-ribbon strong { font-weight: 600; }
  .front-address { position: absolute; left: 330px; width: 420px; top: 456px; text-align: center; font-size: 14px; }

  /* Back */
  .artist-photo {
    position: absolute; left: 0; top: 0; width: 379px; height: 199px;
    background: linear-gradient(100deg, #c8a8a8 0%, #9c7d86 25%, #3b4f6a 45%, #2a2a2e 58%, #e4e2de 78%, #5e6a7c 100%);
  }
  .postcard--back .title-band { left: 0; width: 379px; top: 199px; height: 88px; border-right: 2px solid #fff; }
  .postcard--back .artist-name { font-size: 36px; }
  .postcard--back .artist-role { font-size: 11.5px; margin-top: 4px; }
  .postcard--back .event-type { font-size: 12.5px; margin-top: 4px; }
  .back-date { position: absolute; left: 34px; width: 322px; top: 304px; text-align: center; font-size: 16px; }
  .back-rule { position: absolute; left: 34px; width: 322px; top: 332px; border-top: 1px solid var(--rule); }
  .postcard--back .event-details { left: 20px; width: 350px; top: 344px; font-size: 13.5px; line-height: 1.28; }
  .contact-band {
    position: absolute; left: 0; width: 379px; top: 432px; height: 61px;
    background: var(--band); color: #fff; text-align: center;
  }
  .contact-main { font-size: 14px; margin-top: 10px; display: flex; justify-content: center; align-items: center; gap: 7px; }
  .contact-main svg { width: 14px; height: 14px; }
  .contact-sub { font-size: 10px; margin-top: 7px; }
  .postcard--back .gallery-name { left: 405px; width: 210px; top: 36px; font-size: 18px; }
  .return-address { position: absolute; left: 425px; top: 108px; font-size: 11.5px; line-height: 1.3; }
  .stamp-box { position: absolute; left: 637px; top: 41px; width: 100px; height: 63px; border: 1px solid var(--line); }
  .address-line { position: absolute; left: 422px; width: 315px; border-top: 1px solid var(--line); }
</style>
</head>
<body>

<section class="postcard postcard--front">
  <div class="feature-painting" role="img" aria-label="Impressionist oil painting of tall trees before a sunlit white house"></div>
  <div class="gallery-name">Pinecrest Harbor<br>Galleries</div>
  <div class="title-band">
    <h1 class="artist-name">Rick Dalberson</h1>
    <p class="artist-role">American Impressionist</p>
    <p class="event-type">- OUTDOOR OIL PAINTING DEMONSTRATION -</p>
  </div>
  <p class="event-details">Sunday, September 2 from 1-3 pm<br>in the Pinecrest Harbor Galleries Courtyard<br>Refreshments will be served and all are welcome.</p>
  <p class="artist-quote"><span class="mark">&ldquo;</span>In 2 hours I entertain you by showing how to paint from a photo upside down, (no, not me upside down, the painting). It is the day after my reception, Saturday, September 1 from 4-7 pm, with an artist introduction and brief talk at 5 pm. My show of new and original paintings hangs in The Lantern Gallery from August 22 - September 18. Everyone is welcome.</p>
  <div class="web-ribbon">www.<strong>pinecrestharbor</strong>.com</div>
  <p class="front-address">2250 Lakeshore Bluff Road | Cedar Inlet WI 54900</p>
</section>

<section class="postcard postcard--back">
  <div class="artist-photo" role="img" aria-label="Photo of the artist standing beside his framed harbor painting"></div>
  <div class="title-band">
    <h2 class="artist-name">Rick Dalberson</h2>
    <p class="artist-role">American Impressionist</p>
    <p class="event-type">- OUTDOOR OIL PAINTING DEMONSTRATION -</p>
  </div>
  <p class="back-date">Sunday, September 2 from 1-3 pm</p>
  <div class="back-rule"></div>
  <p class="event-details">in the Pinecrest Harbor Galleries Courtyard<br>Show: Lantern Gallery, August 22 - September 18<br>Reception: Saturday, September 1 from 4-7 pm<br>with an artist introduction and brief talk at 5 pm.</p>
  <div class="contact-band">
    <p class="contact-main">CONTACT US
      <svg viewBox="0 0 16 16" aria-hidden="true"><circle cx="8" cy="8" r="7" fill="none" stroke="#fff" stroke-width="1.3"/><path d="M5.4 4.5l1.3 1.6-.7 1c.5 1 1.3 1.8 2.3 2.3l1-.7 1.6 1.3-.7 1.1c-2.6-.3-4.9-2.6-5.2-5.2z" fill="#fff"/></svg>
      920.555.0148</p>
    <p class="contact-sub">pinecrestharbor@mail.com &nbsp;|&nbsp; www.pinecrestharbor.com</p>
  </div>
  <div class="gallery-name">Pinecrest Harbor<br>Galleries</div>
  <p class="return-address">2250 Lakeshore Bluff Road<br>Cedar Inlet WI 54900</p>
  <div class="stamp-box"></div>
  <div class="address-line" style="top:212px"></div>
  <div class="address-line" style="top:253px"></div>
  <div class="address-line" style="top:294px"></div>
  <div class="address-line" style="top:334px"></div>
</section>

</body>
</html>
```